My Journey - Document to be Laminated

I need a document that is professionally designed. Attached are the files that you are needed to produce this document. The main file to follow is called "My Journey - DOC". I would like you to take the concept and produce it professionally. I think it is important to know that this is something that will be laminated and used by door-to-door representatives. So I need it to be designed in Photoshop so that I can change the pictures as needed to fit other students. The students go to the doors and share literature to help people with their health and to grow spiritually. This document will be something they will share to help the people at the door understand who they are and some of their goals in life. If possible, I would like the concept(s) of the attached picture "theme" to be in the background of all the images - but I still don't want it to be busy, so if it is even something in vector background that is fine.

Not sure why the upload function is not working on pixel harbor for this project. So to download the files, please see the following link: https://www.vaultquill.net/sh/qk7wtz3pxr9mlevjc2hb/Pics-for-Document.zip?key=tr5nq8vmz2hxw4cjl6pa0yd1e&v=7kpz3wqe&get=0

Requirements
Should not have
• anyone with jewelry, more on the minimalistic side

```html
<!DOCTYPE html>
<html lang="en">
<head>
<meta charset="utf-8">
<title>My Journey</title>
<link rel="stylesheet" href="https://fonts.googleapis.com/css2?family=Playfair+Display:wght@500&family=Kaushan+Script&display=swap">
<style>
  :root{
    --sky-top:#3a3a40;
    --sky-mid:#8a7262;
    --sun:#e9a43a;
    --dusk:#6e5a55;
    --ground:#1b1718;
    --paper:#ffffff;
    --wood-light:#c99a66;
    --wood:#b07a45;
    --wood-dark:#7a4e28;
    --ink-red:#8e2a16;
    --tape:rgba(235,235,235,.55);
    --brand:#c8242c;
  }
  *{margin:0;padding:0;box-sizing:border-box}
  html,body{width:960px;height:1200px;overflow:hidden;background:#d9d9d9}
  .poster{position:relative;width:960px;height:1200px;overflow:hidden}
  .backdrop{position:absolute;inset:0;
    background:
      radial-gradient(ellipse 60% 18% at 50% 30%, rgba(245,190,80,.85), rgba(245,190,80,0) 70%),
      linear-gradient(180deg,var(--sky-top) 0%,#6a5a55 14%,var(--sun) 30%,#c98a4a 42%,var(--sky-mid) 55%,var(--dusk) 68%,#3a3032 84%,var(--ground) 100%);}
  .title{position:absolute;left:0;right:0;top:70px;text-align:center;
    font-family:"Playfair Display",serif;font-weight:500;font-size:130px;
    color:var(--paper);letter-spacing:1px;line-height:1}

  .signpost{position:absolute;left:424px;top:276px;width:64px;height:924px;
    background:linear-gradient(90deg,var(--wood-light),var(--wood) 60%,var(--wood-dark))}
  .sign{position:absolute;width:316px;height:110px}
  .sign-board{position:absolute;inset:0;
    background:linear-gradient(180deg,var(--wood-light),var(--wood) 70%,var(--wood-dark))}
  .sign-label{position:absolute;inset:0;display:flex;align-items:center;justify-content:center;
    font-family:"Kaushan Script",cursive;font-size:48px;color:var(--ink-red);line-height:1}
  .sign--roots{left:296px;top:298px;transform:rotate(-5deg)}
  .sign--growing{left:288px;top:490px;transform:rotate(-4deg)}
  .sign--family{left:296px;top:706px;transform:rotate(3deg)}
  .sign--dream{left:280px;top:932px;transform:rotate(-4deg);width:320px;height:104px}

  .snapshot{position:absolute;background:var(--paper);padding:14px;
    box-shadow:0 6px 14px rgba(0,0,0,.35)}
  .snapshot-image{width:100%;height:100%}
  .snapshot--map{left:60px;top:250px;width:272px;height:256px;transform:rotate(4deg)}
  .snapshot--map .snapshot-image{background:linear-gradient(160deg,#c9ccc8 0%,#b3c4c9 40%,#a9d4e4 70%,#b5dbe8 100%)}
  .snapshot--kids{left:612px;top:424px;width:280px;height:262px;transform:rotate(3deg)}
  .snapshot--kids .snapshot-image{background:linear-gradient(180deg,#c8c8d0 0%,#bdbcc4 60%,#a8a6ac 100%)}
  .snapshot--family{left:64px;top:626px;width:270px;height:258px;transform:rotate(-4deg)}
  .snapshot--family .snapshot-image{background:linear-gradient(180deg,#b9b8b4 0%,#5a5658 50%,#2a2628 100%)}
  .snapshot--grad{left:572px;top:832px;width:292px;height:288px;transform:rotate(-5deg)}
  .snapshot--grad .snapshot-image{background:linear-gradient(180deg,#9fb3c9 0%,#e8b889 40%,#8a7f78 62%,#4d4b4e 100%)}
  .tape{position:absolute;background:var(--tape)}
  .tape--map{left:30px;top:262px;width:118px;height:36px;transform:rotate(-40deg)}
  .tape--kids{left:590px;top:410px;width:126px;height:36px;transform:rotate(-14deg)}
  .tape--family{left:258px;top:862px;width:120px;height:36px;transform:rotate(-40deg)}
  .tape--grad{left:790px;top:822px;width:120px;height:36px;transform:rotate(38deg)}
  .brand{position:absolute;left:56px;top:1080px;display:flex;align-items:center;gap:12px}
  .brand-dot{width:34px;height:34px;border-radius:50%;background:var(--brand)}
  .brand-name{font-family:"Playfair Display",serif;font-weight:500;font-size:30px;color:var(--brand)}
</style>
</head>
<body>
<main class="poster">
  <div class="backdrop" role="img" aria-label="Sunset sky over mountain ridges with silhouettes of one hiker helping another up"></div>

  <h1 class="title">MY JOURNEY</h1>

  <div class="signpost" role="img" aria-label="Wooden signpost"></div>

  <div class="snapshot snapshot--map"><div class="snapshot-image" role="img" aria-label="Map of Mexico with a pin marking Mexico City"></div></div>
  <div class="snapshot snapshot--kids"><div class="snapshot-image" role="img" aria-label="Childhood photo of three young sisters"></div></div>
  <div class="snapshot snapshot--family"><div class="snapshot-image" role="img" aria-label="Family photo of four people at an airport"></div></div>
  <div class="snapshot snapshot--grad"><div class="snapshot-image" role="img" aria-label="Graduate in cap and gown overlooking a city skyline at sunset"></div></div>

  <div class="tape tape--map"></div>
  <div class="tape tape--kids"></div>
  <div class="tape tape--family"></div>
  <div class="tape tape--grad"></div>

  <div class="sign sign--roots">
    <div class="sign-board" role="img" aria-label="Wooden arrow sign pointing left"></div>
    <span class="sign-label">My Roots</span>
  </div>
  <div class="sign sign--growing">
    <div class="sign-board" role="img" aria-label="Wooden arrow sign pointing right"></div>
    <span class="sign-label">Growing up</span>
  </div>
  <div class="sign sign--family">
    <div class="sign-board" role="img" aria-label="Wooden arrow sign pointing left"></div>
    <span class="sign-label">My Family</span>
  </div>
  <div class="sign sign--dream">
    <div class="sign-board" role="img" aria-label="Wooden arrow sign pointing right"></div>
    <span class="sign-label">My Dream</span>
  </div>

  <div class="brand">
    <span class="brand-dot"></span>
    <span class="brand-name">Maple Trail Youth</span>
  </div>
</main>
</body>
</html>
```